Business Card and Letterhead for Nurlo - modern real estate business

I need a double sided business card design for Nurlo. Please see business card brief here https://papers.trelvimo.net/sheet/q/7XrTbaLeZpMmQ2uWvd9HkCj4yNoEfsGi3lRtAz_pk/view?mode=shared

Please feel free to design the business cards however you feel best. I am happy to give some creative freedoms and then provide feedback from there.

Please then also create a letterhead to match the business card design

Colors

Designer to choose colors to be used in the design.

Requirements
Must have
• Must be a modern, elegant business card which looks very professional

```html
<!DOCTYPE html>
<html lang="en">
<head>
<meta charset="utf-8">
<title>Nurlo Business Card</title>
<link href="https://fonts.googleapis.com/css2?family=Poppins:wght@400;500;600&display=swap" rel="stylesheet">
<style>
  :root {
    --brand-red: #e3262c;
    --ink: #111111;
    --card-black: #000000;
    --card-white: #ffffff;
    --backdrop: #d6d4d2;
    --photo-dark: #2b2b2d;
    --photo-light: #c9bfb6;
  }
  * { box-sizing: border-box; margin: 0; padding: 0; }
  html, body { width: 1200px; height: 800px; overflow: hidden; }
  body {
    background: var(--backdrop);
    font-family: "Poppins", sans-serif;
    color: var(--ink);
    position: relative;
  }
  .card {
    position: absolute;
    width: 608px;
    height: 376px;
    box-shadow: 0 6px 18px rgba(0,0,0,0.25);
  }
  .card-front {
    left: 81px; top: 57px;
    background: var(--card-black);
    display: flex; align-items: center; justify-content: center;
  }
  .brand-name {
    font-family: "Poppins", sans-serif;
    font-weight: 600;
    color: var(--brand-red);
    text-transform: uppercase;
    line-height: 1;
  }
  .card-front .brand-name {
    font-size: 72px;
    letter-spacing: 4px;
    margin-top: -8px;
  }
  .card-back {
    left: 505px; top: 370px;
    background: var(--card-white);
    overflow: hidden;
  }
  .card-back .brand-name {
    position: absolute;
    left: 40px; top: 52px;
    font-size: 52px;
    letter-spacing: 3px;
  }
  .agent-name {
    position: absolute;
    left: 40px; top: 160px;
    font-size: 21px;
    font-weight: 600;
  }
  .agent-role {
    position: absolute;
    left: 40px; top: 190px;
    font-size: 14px;
  }
  .address {
    position: absolute;
    left: 40px; top: 223px;
    font-size: 12.5px;
    line-height: 19px;
    font-style: normal;
  }
  .contact-list {
    position: absolute;
    left: 40px; top: 269px;
    list-style: none;
    font-size: 12.5px;
    line-height: 19px;
  }
  .contact-list li { display: flex; align-items: center; gap: 6px; }
  .contact-list svg { width: 10px; height: 10px; fill: var(--ink); flex: none; }
  .portrait {
    position: absolute;
    left: 273px; top: 23px;
    width: 326px; height: 353px;
    background: linear-gradient(180deg, var(--photo-light) 0%, #8a7e76 30%, var(--photo-dark) 55%, var(--photo-dark) 100%);
    clip-path: polygon(38% 0, 62% 0, 66% 30%, 92% 42%, 100% 100%, 0 100%, 5% 44%, 34% 30%);
  }
</style>
</head>
<body>
  <section class="card card-front">
    <span class="brand-name">Nurlo</span>
  </section>

  <section class="card card-back">
    <span class="brand-name">Nurlo</span>
    <h1 class="agent-name">Liam Carter</h1>
    <p class="agent-role">Licenced Real Estate Agent</p>
    <address class="address">PO Box 5170<br>Ashbrook NSW 2791</address>
    <ul class="contact-list">
      <li><svg viewBox="0 0 10 10"><path d="M1 3 Q5 0 9 3 L8 4 L6.5 3.5 L6.5 2.8 Q5 2.4 3.5 2.8 L3.5 3.5 L2 4 Z M2.5 5 L7.5 5 L8.5 9 L1.5 9 Z"/></svg>0412 555 019</li>
      <li><svg viewBox="0 0 10 10"><path d="M1 3 Q5 0 9 3 L8 4 L6.5 3.5 L6.5 2.8 Q5 2.4 3.5 2.8 L3.5 3.5 L2 4 Z M2.5 5 L7.5 5 L8.5 9 L1.5 9 Z"/></svg>1300 555 210</li>
      <li><svg viewBox="0 0 10 10"><path d="M0.5 2 H9.5 V8 H0.5 Z M1 2.5 L5 5.5 L9 2.5" stroke="#fff" stroke-width="0.8"/></svg>liam@nurlo.com</li>
      <li><svg viewBox="0 0 10 10"><circle cx="5" cy="5" r="4.5"/><path d="M0.5 5 H9.5 M5 0.5 V9.5 M5 0.5 Q2 5 5 9.5 M5 0.5 Q8 5 5 9.5" stroke="#fff" stroke-width="0.6" fill="none"/></svg>www.nurlo.com</li>
    </ul>
    <div class="portrait" role="img" aria-label="Portrait photo of the agent in a dark suit and shirt"></div>
  </section>
</body>
</html>
```